A sustainable tourism website

We are a travel/tourism company. We have developed a platform that enables organizers of sustainable theme vacations to publish and make their vacations bookable via our platform. By theme vacations, we mean vacations in categories such as Wellness, Surfing, Culinary, Martial arts, etc. We already have separate websites for each of these categories. This new website you will design is about a parent site where we provide general summary information about these individual sites and link to them. The site would be hosted on the domain veloramix.com. Besides information about the individual sites, we also need a menu for About Us, Products and Our Climate Pledge. We also need the following at the home page:
1. A section that contain our last tweets in a twitter lightbox.
2. Summary and links to of our last few blogs.
3. A video as banner or an image. We would prefer a video though.
We already have a logo and have uploaded it. Please make sure your design conforms with our logo style and colors.
NB: We are looking for something more than the standard site you see everywhere. The winning design is a design that stands out and has a WOW effect. And when your design is selected, we intend to work with you further for the completion of the whole site.

Target Market(s)

Sustainable tourism

Number of Pages Required

1 page

Requirements
Must have
• Conform to logo design and colors.
Site must be unique, slick and stand out.
Must have a climate/sustainability blended with tourism look.
Nice to have
• Video as banner.

```html
<!DOCTYPE html>
<html lang="en">
<head>
<meta charset="utf-8">
<title>veloramix — Tours, Trips, Treks &amp; Travel</title>
<link href="https://fonts.googleapis.com/css2?family=Bebas+Neue&family=Poppins:ital,wght@0,300;0,400;0,500;0,600;0,700;1,300;1,400&display=swap" rel="stylesheet">
<style>
:root{
  --orange:#f7941d;
  --orange-deep:#ef8a12;
  --ink:#1b1b1b;
  --text:#555;
  --muted:#888;
  --line:#e6e6e6;
  --white:#fff;
  --star:#1f5fa8;
}
*{margin:0;padding:0;box-sizing:border-box}
html,body{width:1200px;height:4831px;overflow:hidden}
body{position:relative;background:var(--white);font-family:'Poppins',sans-serif;color:var(--text)}
.abs{position:absolute}
.heading{font-family:'Bebas Neue',sans-serif;color:var(--ink);font-weight:400;line-height:.9}

/* header & hero */
.hero{left:0;top:0;width:1200px;height:803px;
  background:
    radial-gradient(ellipse 260px 420px at 150px 260px,#c9d3d2 0%,#9fb0ae 40%,transparent 75%),
    radial-gradient(ellipse 380px 260px at 330px 620px,#b8c8c6 0%,#7f938f 50%,transparent 80%),
    radial-gradient(ellipse 240px 380px at 850px 470px,#8f7a3e 0%,#5e5634 45%,transparent 80%),
    radial-gradient(ellipse 300px 300px at 1080px 160px,#4f6a3a 0%,transparent 75%),
    linear-gradient(100deg,#4a5856 0%,#6f7f7a 28%,#55604a 55%,#344030 80%,#26321f 100%)}
.hero-shade{left:0;top:0;width:1200px;height:803px;background:linear-gradient(180deg,#0004 0%,transparent 18%,transparent 80%,#0003 100%)}
.logo{display:flex;align-items:center;gap:6px;font-weight:400;color:var(--orange);font-size:34px;letter-spacing:-.5px;line-height:1}
.logo .dot{width:26px;height:26px;border:2px solid var(--orange);border-radius:50%}
.nav{left:433px;top:38px;display:flex;gap:29px;font-size:12px;font-weight:600;color:var(--white);letter-spacing:.3px}
.lang{display:flex;align-items:center;gap:4px;font-weight:400}
.lang i{width:14px;height:9px;background:#c8313e;display:inline-block}
.btn-book{left:982px;top:29px;width:129px;height:36px;background:var(--orange);color:var(--white);font-size:12px;font-weight:600;display:flex;align-items:center;justify-content:center;border:1px solid #fff3}
.hero-title{left:86px;top:352px;font-size:80px;color:var(--white)}
.play{left:88px;top:502px;display:flex;align-items:center;gap:14px;color:var(--white);font-size:12px;font-weight:600}
.play .circle{width:66px;height:66px;border-radius:50%;background:var(--white);display:flex;align-items:center;justify-content:center}

/* search */
.search{left:133px;top:769px;width:932px;height:58px;background:var(--white);box-shadow:0 8px 24px #0002;display:flex;font-size:13px;color:#444}
.search .field{display:flex;align-items:center;justify-content:space-between;padding:0 20px;border-right:1px solid var(--line)}
.search .go{margin-left:auto;width:191px;background:var(--orange);color:var(--white);font-weight:600;display:flex;align-items:center;justify-content:center;gap:8px}

/* wave backdrop */
.wave{left:0;top:930px;width:1200px;height:1160px;
  background:
    radial-gradient(ellipse 420px 520px at 1110px 420px,#2fc4b8 0%,#5fd4c8 30%,#a8e6df 60%,transparent 85%),
    radial-gradient(ellipse 300px 260px at 60px 440px,#c8d4d6 0%,#e4ebec 50%,transparent 85%),
    radial-gradient(ellipse 700px 200px at 600px 1090px,#dfeff0 0%,transparent 80%),
    linear-gradient(180deg,#fff 0%,#f3f8f8 40%,#eef6f6 80%,#fff 100%)}

/* tour cards */
.card{top:919px;width:296px;height:375px;background:var(--white);border:1px solid var(--line);box-shadow:0 2px 8px #0001}
.card .media{height:225px;position:relative}
.price{position:absolute;left:0;bottom:22px;background:#555c;color:var(--white);font-size:20px;padding:5px 20px}
.price.hot{background:var(--orange)}
.card h3{font-size:28px;margin:38px 0 0 23px}
.card .place{font-size:15px;margin:4px 0 0 23px}
.meta{display:flex;align-items:center;margin:10px 0 0 23px;font-size:13px;color:#333;gap:16px}
.stars{color:var(--star);letter-spacing:2px;font-size:13px}
.stars.gold{color:var(--orange)}
.stars b{color:#bbb;font-weight:400}
.days{display:flex;align-items:center;gap:5px}

/* about */
.about-photo{left:456px;top:1294px;width:654px;height:724px;
  background:
    radial-gradient(ellipse 160px 200px at 420px 150px,#8a6a52 0%,#5a4436 50%,transparent 85%),
    radial-gradient(ellipse 260px 200px at 560px 120px,#9fe0d6 0%,#d8f0ec 50%,transparent 85%),
    radial-gradient(ellipse 260px 220px at 120px 560px,#e6eaea 0%,#b8c2c2 45%,transparent 85%),
    radial-gradient(ellipse 260px 260px at 400px 520px,#2a2420 0%,#3d3430 55%,transparent 90%),
    linear-gradient(165deg,#cfd9d8 0%,#6a5c52 40%,#2d2a28 70%,#7c868a 100%)}
.about-box{left:88px;top:1528px;width:482px;height:411px;background:linear-gradient(135deg,#f8a02a,var(--orange-deep));padding:100px 60px 0}
.about-box h2{font-size:56px;color:var(--white)}
.about-box p{font-size:13.5px;line-height:23px;color:var(--white);margin-top:14px}
.btn-read{display:inline-block;margin-top:18px;background:var(--white);color:var(--ink);font-size:13px;font-weight:600;padding:7px 20px}

/* gallery */
.section-title{width:1200px;text-align:center;font-size:60px}
.tile{position:absolute}
.counter{position:absolute;bottom:26px;color:var(--white);font-size:12px}
.feature-label{left:681px;top:2383px;display:flex;align-items:center;gap:15px;color:var(--white);font-size:12px;font-weight:600}
.feature-label i{width:24px;height:24px;border:2px solid var(--white);border-radius:4px}
.feature-title{left:677px;top:2498px;font-size:44px;font-weight:600;color:var(--white);line-height:44px}
.feature-link{left:682px;top:2652px;color:var(--orange);font-size:12px;font-weight:600;display:flex;gap:8px;align-items:center}
.accent-bar{left:619px;top:2470px;width:7px;height:162px;background:var(--orange)}
.vertical{left:1112px;top:2520px;transform:rotate(-90deg);transform-origin:left top;font-size:10px;letter-spacing:1px;color:#333}
.vline{left:1121px;top:2530px;width:2px;height:68px;background:#222}

/* blog */
.blog-bg{left:0;top:2809px;width:1200px;height:700px;
  background:
    radial-gradient(ellipse 420px 300px at 200px 120px,#4e5a5e 0%,#7f8c8e 45%,transparent 85%),
    radial-gradient(ellipse 300px 120px at 460px 250px,#6fb3b0 0%,#a9d3cf 50%,transparent 85%),
    radial-gradient(ellipse 600px 160px at 700px 30px,#aab3b5 0%,transparent 80%),
    linear-gradient(180deg,#c9cfd0 0%,#f2f3f3 35%,#fff 60%)}
.blog-card{top:3054px;width:325px;height:402px;background:var(--white);box-shadow:0 2px 10px #0001}
.blog-card .media{height:244px}
.blog-card .by{font-size:11px;color:#555;margin:28px 0 0 27px}
.blog-card h4{font-family:'Bebas Neue',sans-serif;font-size:22px;color:var(--ink);line-height:24px;margin:12px 27px 0;font-weight:400}
.tag{display:inline-block;margin:8px 0 0 27px;background:#fdebd3;color:var(--orange);font-size:9px;padding:3px 22px;border-radius:10px}
.more{left:0;top:3497px;width:1200px;text-align:center;font-size:13px;color:#555}

/* testimonials */
.quote-mark{font-family:'Bebas Neue',sans-serif;font-size:200px;color:#ececec;line-height:1}
.avatar{width:127px;height:127px;border-radius:50%;border:5px solid var(--white);box-shadow:0 4px 14px #0002}
.testi{font-size:13px;font-style:italic;font-weight:300;line-height:29px;color:#555;width:310px}
.testi strong{display:block;font-style:normal;font-weight:500;font-size:15px;color:var(--ink);margin-top:2px}

/* sea & footer */
.sea{left:0;top:3860px;width:1200px;height:971px;
  background:
    radial-gradient(ellipse 700px 90px at 900px 360px,#f4f4f4 0%,#cfcfcf 45%,transparent 85%),
    radial-gradient(ellipse 520px 80px at 260px 420px,#ececec 0%,#bdbdbd 45%,transparent 85%),
    radial-gradient(ellipse 900px 130px at 600px 470px,#6e6e6e 0%,transparent 85%),
    radial-gradient(ellipse 500px 120px at 820px 290px,#8a8a8a 0%,transparent 85%),
    radial-gradient(ellipse 180px 60px at 620px 690px,#3f3f3f 0%,transparent 85%),
    linear-gradient(180deg,#fff 0%,#f1f1f1 12%,#cdcdcd 26%,#a8a8a8 36%,#8e8e8e 48%,#7a7a7a 58%,#6a6a6a 70%,#535353 85%,#3e3e3e 100%)}
.foot-col{color:var(--white);font-size:12.5px;line-height:22px}
.foot-col h5{font-size:20px;font-weight:500;margin-bottom:12px}
.social{display:flex;gap:10px;margin-top:14px}
.social i{width:22px;height:22px;border-radius:50%;border:1px solid #fff8}
.email{width:324px;height:40px;background:#fff2;border:1px solid #fff3;color:#ddd;font-size:11px;padding:12px 20px}
.btn-sub{display:inline-block;margin-top:14px;background:var(--orange);color:var(--white);font-size:12px;font-weight:600;padding:8px 20px}
.rule{left:99px;top:4772px;width:1012px;height:1px;background:#fff4}
.copy{left:0;top:4796px;width:1200px;text-align:center;color:var(--white);font-size:13px}
.top-btn{left:1130px;top:4760px;width:32px;height:32px;border-radius:50%;background:var(--orange);display:flex;align-items:center;justify-content:center}
</style>
</head>
<body>

<!-- hero -->
<div class="abs hero" role="img" aria-label="Traveller in a hat holding a map beside a waterfall"></div>
<div class="abs hero-shade"></div>
<div class="abs logo" style="left:88px;top:30px">veloramix<span class="dot"></span></div>
<nav class="abs nav">
  <span>ABOUT</span><span>PRODUCTS</span><span>CLIMATE PLEDGE</span><span>BLOG</span><span>CONTACT</span>
  <span class="lang"><i></i>Eng ▾</span>
</nav>
<div class="abs btn-book">BOOK A TOUR</div>
<h1 class="abs heading hero-title">TOURS TRIPS<br>TREKS &amp; TRAVEL</h1>
<div class="abs play">
  <span class="circle"><svg width="20" height="22" viewBox="0 0 20 22"><path d="M2 1 L19 11 L2 21Z" fill="#f7941d"/></svg></span>
  PLAY VIDEO
</div>

<!-- search -->
<div class="abs search">
  <div class="field" style="width:283px">Select Tour <span>⌄</span></div>
  <div class="field" style="width:234px">Travel Month
    <svg width="16" height="14" viewBox="0 0 16 14"><rect x="1" y="2" width="14" height="11" fill="none" stroke="#999"/><line x1="1" y1="5" x2="15" y2="5" stroke="#999"/></svg></div>
  <div class="field" style="width:223px;border:none">Guests 1 <span>⌄</span></div>
  <div class="go"><svg width="13" height="13" viewBox="0 0 13 13"><circle cx="5.5" cy="5.5" r="4.3" fill="none" stroke="#fff" stroke-width="1.6"/><line x1="8.7" y1="8.7" x2="12" y2="12" stroke="#fff" stroke-width="1.6"/></svg>SEARCH</div>
</div>

<!-- wave backdrop -->
<div class="abs wave" role="img" aria-label="Turquoise ocean wave breaking with spray"></div>

<!-- tour cards -->
<div class="abs card" style="left:135px">
  <div class="media" role="img" aria-label="Scuba diver underwater" style="background:radial-gradient(ellipse 90px 80px at 150px 90px,#d8b48a 0%,transparent 80%),radial-gradient(ellipse 60px 120px at 20px 60px,#8a7a6a 0%,transparent 80%),linear-gradient(160deg,#3a9ac0,#15608e 55%,#0a2e4c)"><span class="price">$5,000</span></div>
  <h3 class="heading">DIVING CENTER</h3>
  <p class="place">City Tours, Thailand</p>
  <div class="meta"><span class="stars">★★★★<b>★</b></span><span>4 Reviews</span><span class="days"><svg width="13" height="13"><circle cx="6.5" cy="6.5" r="5.5" fill="none" stroke="#333"/><path d="M6.5 3v3.5h2.5" fill="none" stroke="#333"/></svg>5 days</span></div>
</div>
<div class="abs card" style="left:450px">
  <div class="media" role="img" aria-label="Surfer riding a blue wave" style="background:radial-gradient(ellipse 120px 70px at 120px 90px,#f2f7fa 0%,transparent 80%),radial-gradient(ellipse 90px 40px at 240px 190px,#d9c6a2 0%,transparent 85%),linear-gradient(180deg,#9fd3ea,#3a9ad0 45%,#0f4f8a)"><span class="price hot">$5,000</span></div>
  <h3 class="heading">WATER SPORT</h3>
  <p class="place">City Tours, Thailand</p>
  <div class="meta"><span class="stars gold">★★★★<b>★</b></span><span>4 Reviews</span><span class="days"><svg width="13" height="13"><circle cx="6.5" cy="6.5" r="5.5" fill="none" stroke="#333"/><path d="M6.5 3v3.5h2.5" fill="none" stroke="#333"/></svg>5 days</span></div>
</div>
<div class="abs card" style="left:765px">
  <div class="media" role="img" aria-label="Group of hikers looking out over a lake" style="background:radial-gradient(ellipse 170px 50px at 150px 200px,#3a3650 0%,transparent 85%),linear-gradient(180deg,#2c7da8,#1e6a92 65%,#5a6a60)"><span class="price">$5,000</span></div>
  <h3 class="heading">URBAN TOURS</h3>
  <p class="place">City Tours, Thailand</p>
  <div class="meta"><span class="stars">★★★★<b>★</b></span><span>4 Reviews</span><span class="days"><svg width="13" height="13"><circle cx="6.5" cy="6.5" r="5.5" fill="none" stroke="#333"/><path d="M6.5 3v3.5h2.5" fill="none" stroke="#333"/></svg>5 days</span></div>
</div>

<!-- about -->
<div class="abs about-photo" role="img" aria-label="Hiker with backpack standing on coastal rocks as waves crash"></div>
<div class="abs about-box">
  <h2 class="heading">ABOUT<br>TOURISTS</h2>
  <p>Lorem Ipsum is simply dummy text of the printing and typesetting industry. Lorem Ipsum has been the industry's standard dummy text ever since the 1500s, when an unknown printer took.</p>
  <span class="btn-read">READ MORE</span>
</div>

<!-- world of tourists -->
<h2 class="abs heading section-title" style="left:0;top:2146px">WORLD OF TOURISTS</h2>
<div class="tile" role="img" aria-label="Friends taking a selfie at a fair" style="left:0;top:2244px;width:191px;height:186px;background:radial-gradient(ellipse 60px 70px at 140px 80px,#e8c0a0 0%,transparent 80%),linear-gradient(135deg,#d2584a,#e8b86a 45%,#6a9fc0 75%,#e8e8e8)"></div>
<div class="tile" role="img" aria-label="Close view of a camera lens" style="left:0;top:2440px;width:191px;height:369px;background:radial-gradient(circle at 40px 250px,#1a1a1a 0%,#3a3a3a 35%,transparent 60%),linear-gradient(135deg,#6a7580,#a9b2ba 40%,#c7a25a 75%,#e2b24c)"><span class="counter" style="left:150px">01/25</span></div>
<div class="tile" role="img" aria-label="Hiker with red backpack walking through a forest" style="left:201px;top:2244px;width:410px;height:565px;background:radial-gradient(ellipse 60px 80px at 205px 380px,#d8343c 0%,transparent 80%),radial-gradient(ellipse 200px 200px at 200px 130px,#f6f8e8 0%,#c8d8a0 45%,transparent 85%),linear-gradient(170deg,#d8e4c0,#8aa860 40%,#6b7a3e 70%,#a8865a)">
  <span style="position:absolute;left:42px;bottom:30px;width:30px;height:30px;border-radius:50%;background:var(--orange);display:flex;align-items:center;justify-content:center"><svg width="10" height="12"><path d="M1 1L9 6L1 11Z" fill="#fff"/></svg></span>
  <span class="counter" style="right:14px">01/25</span>
</div>
<div class="tile" role="img" aria-label="Photographer with a camera overlooking mountains" style="left:622px;top:2244px;width:413px;height:565px;background:radial-gradient(ellipse 130px 200px at 300px 440px,#1e2422 0%,transparent 85%),radial-gradient(ellipse 260px 120px at 300px 60px,#c4cacb 0%,transparent 85%),linear-gradient(160deg,#a9b0b2,#6d7b76 40%,#3a4440 80%,#2b302e)"></div>
<div class="abs accent-bar"></div>
<div class="abs feature-label"><i></i>PHOTOGRAPHY</div>
<div class="abs feature-title">Urban<br>tours</div>
<div class="abs feature-link">FULL STORY <svg width="18" height="10"><path d="M0 5h16M12 1l4 4-4 4" fill="none" stroke="#f7941d" stroke-width="1.4"/></svg></div>
<div class="abs vertical">DISTINATIONS</div>
<div class="abs vline"></div>

<!-- blog -->
<div class="abs blog-bg" role="img" aria-label="Traveller sitting on a cliff above a turquoise bay"></div>
<h2 class="abs heading section-title" style="left:0;top:2965px">LATEST BLOG</h2>
<div class="abs blog-card" style="left:77px">
  <div class="media" role="img" aria-label="Woman sitting on a car roof on a sunny road" style="background:radial-gradient(ellipse 70px 90px at 140px 110px,#f0c020 0%,transparent 80%),radial-gradient(ellipse 120px 50px at 150px 215px,#e8e8e8 0%,transparent 85%),linear-gradient(180deg,#f5e3b6,#f2c260 40%,#c9a86a 75%,#8a7a5a)"></div>
  <p class="by">by Alden R. • 17 hours ago</p>
  <h4>BLOG 1 HEADING: SOME NEWS<br>HEADING GOES HERE...</h4>
  <span class="tag">BLOG</span>
</div>
<div class="abs blog-card" style="left:426px">
  <div class="media" role="img" aria-label="Red suspension bridge rising out of fog" style="background:radial-gradient(ellipse 40px 140px at 90px 110px,#a8402e 0%,transparent 85%),linear-gradient(180deg,#5f88b0,#9fb8cc 50%,#e2e8ec)"></div>
  <p class="by">by Tessa Lund • 18 hours ago</p>
  <h4>NEWS 2 HEADING: SOME NEWS<br>HEADING GOES HERE...</h4>
  <span class="tag">NEWS</span>
</div>
<div class="abs blog-card" style="left:774px">
  <div class="media" role="img" aria-label="Outdoor dining table laid with food beside a lake" style="background:radial-gradient(ellipse 140px 50px at 170px 180px,#e8a040 0%,transparent 85%),linear-gradient(180deg,#2f4a32,#557a48 40%,#e4e2dc 70%,#c9b896)"></div>
  <p class="by">by Owen Pryce • 17 hours ago</p>
  <h4>BLOG 3 HEADING: SOME NEWS<br>HEADING GOES HERE...</h4>
  <span class="tag">BLOG</span>
</div>
<p class="abs more">Interested in our News and Blogs ? Check out more</p>

<!-- testimonials over sea backdrop -->
<div class="abs sea" role="img" aria-label="Aerial view of waves on a grey shoreline with whales swimming below"></div>
<h2 class="abs heading section-title" style="left:0;top:3634px">TESTIMONIALS</h2>
<div class="abs quote-mark" style="left:400px;top:3690px">“</div>
<div class="abs quote-mark" style="left:952px;top:3690px">“</div>
<div class="abs avatar" role="img" aria-label="Customer portrait at sunset" style="left:92px;top:3760px;background:radial-gradient(circle at 40% 40%,#f6c86a,#c9762e 60%,#7a3e1a)"></div>
<div class="abs testi" style="left:240px;top:3755px">Lorem Ipsum is simply dummy text of the printing and typesetting industry. Lorem Ipsum has been the industry's standard dummy text ever since the 1500s, when an unknown .<strong>Marena, Toronto, Ontario</strong></div>
<div class="abs avatar" role="img" aria-label="Customer portrait outdoors" style="left:645px;top:3760px;background:radial-gradient(circle at 50% 40%,#e9ecef,#7c8a96 60%,#2e3a44)"></div>
<div class="abs testi" style="left:793px;top:3755px">Lorem Ipsum is simply dummy text of the printing and typesetting industry. Lorem Ipsum has been the industry's standard dummy text ever since the 1500s, when an unknown .<strong>Dorian, Hamilton, ON</strong></div>

<!-- footer -->
<div class="abs foot-col" style="left:99px;top:4568px;width:330px">
  <div class="logo" style="margin-bottom:12px">veloramix<span class="dot"></span></div>
  <p>Lorem ipsum dolor sit amet, consectetuer adipiscing elit. Aenean commodo ligula eget dolor.</p>
  <div class="social"><i></i><i></i><i></i><i></i></div>
</div>
<div class="abs foot-col" style="left:456px;top:4576px">
  <h5>Contact Info</h5>
  <p>1-555-018-000000</p>
  <p style="margin-top:6px">27 Harbor Lane East Coastview 000</p>
  <p style="margin-top:6px">Mon – Sat 8.00 – 18.00 Sunday CLOSED</p>
</div>
<div class="abs foot-col" style="left:780px;top:4576px">
  <h5>Newsletter</h5>
  <div class="email">Email Address</div>
  <span class="btn-sub">SUBSCRIBE</span>
</div>
<div class="abs rule"></div>
<p class="abs copy">Copyright 2019 | All Right Reserved</p>
<div class="abs top-btn"><svg width="12" height="8"><path d="M1 7L6 2L11 7" fill="none" stroke="#fff" stroke-width="1.6"/></svg></div>

</body>
</html>
```